The label Velombri Dijon Mustard

Hello everybody,
What we need : a design for a label of Dijon Mustard it's a new project and. What we're looking for : a european style with a warm vibe. The product's target : the North American.

The design must be elegant, modern and up market.don't hesitate to think outside the box.
we attached a file contain our logo. the logo for this product will be the main logo the third one.
and we attached a sizes and the inspiration design LUVETTE and CORBIN

Target Market(s)

North America

Logo Text

Velombri

Logo styles of interest
Wordmark Logo
Font styles to use
Serif
Script

Colors

Designer to choose colors to be used in the design.

Requirements
Must have
• -The brand ''Velombri'' and the logo is (the Main logo The Third one) attached file.
• - the name of the product, ''Dijon Mustard /Moutarde de Dijon/ ديجون الخردل'', in English, French and Arabic
• -The Lid will be red or black depend of your design.
• - the nutrition fact. Make a place and it will be changed by us.
• -Ingrediants:
• fr: eau, graines de MOUTARDE, vinaigre d'alcool, sel, acidifiant : acide citrique, conservateur : E224 (SULFITES).
• En: water, MUSTARD seeds, alcohol vinegar, salt, acidifier: citric acid, preservative: E224 (SULFITES).
• Ar: ماء ، بذور الخردل ، خل الكحول ، الملح ، محمض: حمض الستريك ، مواد حافظة: E224
• - the weight of 295g/ 250ml
• - conditioned by Sarl Velombri/conditionné par Sarl Velombri.
• -Slogan In French''Apportez le vrai goût à votre maison''
• -design must be elegant, modern and up market.
Nice to have
• -A minimalist design style
• -Design color: red or black.

```html
<!DOCTYPE html>
<html lang="en">
<head>
<meta charset="utf-8">
<title>Velombri Dijon Mustard – Label</title>
<link rel="stylesheet" href="https://fonts.googleapis.com/css2?family=Cinzel:wght@400;700&family=Yellowtail&family=PT+Sans&family=Roboto+Condensed:wght@700&family=Arimo:wght@400;700&display=swap">
<style>
  :root {
    --label-green: #006838;
    --label-green-deep: #004d29;
    --cream: #fdfbe9;
    --slogan-gold: #f6e9a6;
    --brand-red: #d9262a;
    --ink: #111111;
    --paper: #ffffff;
  }
  * { margin: 0; padding: 0; box-sizing: border-box; }
  html, body { width: 1200px; height: 585px; overflow: hidden; background: var(--paper); }
  .canvas { position: relative; width: 1200px; height: 585px; }

  .label { position: absolute; top: 0; width: 560px; height: 585px; }
  .label--front { left: 44px; }
  .label--back { left: 620px; }
  .label__shape { position: absolute; inset: 0; }
  .label__fill { fill: var(--label-green); }
  .label__rule { fill: none; stroke: var(--cream); stroke-width: 1.4; }

  .brand-name {
    position: absolute; left: 0; right: 0; text-align: center;
    font-family: "Cinzel", serif; font-weight: 700; letter-spacing: 1px;
  }
  .label--front .brand-name { top: 78px; font-size: 40px; color: var(--brand-red); }
  .label--back .brand-name { top: 56px; font-size: 32px; color: var(--cream); }

  .product-name {
    position: absolute; left: 0; right: 0; top: 176px; text-align: center;
    font-family: "Cinzel", serif; font-weight: 400; color: var(--cream);
    line-height: 66px; font-size: 74px; letter-spacing: 1px;
    text-shadow: 4px 3px 0 #3fa34d;
  }
  .product-name span { display: block; }

  .slogan {
    position: absolute; left: 0; right: 0; text-align: center;
    font-family: "Yellowtail", cursive;
  }
  .label--front .slogan { top: 356px; font-size: 29px; color: var(--slogan-gold); }
  .label--back .slogan { top: 110px; font-size: 22px; color: var(--cream); }

  .flourish {
    position: absolute; left: 128px; top: 408px; width: 244px; height: 64px;
    background: linear-gradient(90deg, transparent, rgba(253,251,233,.35) 30%, rgba(253,251,233,.35) 70%, transparent);
    border-radius: 32px;
  }

  .net-weight {
    position: absolute; left: 0; right: 0; top: 514px; text-align: center;
    font-family: "Arimo", sans-serif; font-weight: 700; font-size: 18px; color: var(--cream);
  }

  .description {
    position: absolute; left: 70px; top: 166px; width: 190px;
    font-family: "PT Sans", sans-serif; font-size: 12.6px; line-height: 17.6px; color: var(--cream);
  }

  .nutrition {
    position: absolute; left: 282px; top: 146px; width: 146px; height: 276px;
    background: var(--paper); border: 1.5px solid var(--ink); padding: 3px 4px;
    font-family: "Arimo", sans-serif; color: var(--ink); font-size: 6.4px; line-height: 1.25;
  }
  .nutrition__title { font-size: 17px; font-weight: 700; line-height: 17px; }
  .nutrition__row { display: flex; justify-content: space-between; border-top: 0.6px solid var(--ink); padding: 1.4px 0; }
  .nutrition__row--plain { border-top: none; }
  .nutrition__row--indent { padding-left: 8px; }
  .nutrition__row--indent2 { padding-left: 18px; }
  .nutrition__bar { height: 6px; background: var(--ink); margin: 1px 0; }
  .nutrition__bar--mid { height: 3px; }
  .nutrition__serving { font-size: 7.6px; font-weight: 700; }
  .nutrition__calories { display: flex; justify-content: space-between; align-items: flex-end; font-weight: 700; }
  .nutrition__calories-label { font-size: 12.5px; }
  .nutrition__calories-value { font-size: 18px; line-height: 18px; }
  .nutrition__dv { text-align: right; font-weight: 700; font-size: 5.4px; border-top: 0.6px solid var(--ink); padding: 1px 0; }
  .nutrition b { font-weight: 700; }
  .nutrition__footnote { font-size: 4.6px; line-height: 1.25; padding-top: 2px; }

  .ingredients {
    position: absolute; left: 136px; top: 431px; width: 320px;
    font-family: "Arimo", sans-serif; font-size: 11.3px; line-height: 14px; color: var(--cream);
  }
  .packer {
    position: absolute; left: 0; right: 0; top: 514px; text-align: center;
    font-family: "Roboto Condensed", sans-serif; font-weight: 700; font-size: 9.6px; color: var(--cream);
  }
</style>
</head>
<body>
<main class="canvas">

  <section class="label label--front" aria-label="Front label">
    <svg class="label__shape" viewBox="0 0 560 585" aria-hidden="true">
      <defs>
        <path id="label-outline" d="M100 60 C130 60 150 45 160 25 C200 4 360 4 400 25 C410 45 430 60 460 60 C490 60 500 80 500 100 C500 130 515 150 535 160 C560 200 560 385 535 425 C515 435 500 455 500 485 C500 505 490 525 460 525 C430 525 410 540 400 560 C360 581 200 581 160 560 C150 540 130 525 100 525 C70 525 60 505 60 485 C60 455 45 435 25 425 C0 385 0 200 25 160 C45 150 60 130 60 100 C60 80 70 60 100 60 Z"/>
      </defs>
      <use href="#label-outline" class="label__fill"/>
      <use href="#label-outline" class="label__rule" transform="translate(280 292.5) scale(0.975) translate(-280 -292.5)"/>
    </svg>
    <div class="brand-name">Velombri</div>
    <h1 class="product-name"><span>Dijon</span><span>Mustard</span></h1>
    <p class="slogan">Apportez le vrai goût à votre maison</p>
    <div class="flourish" role="img" aria-label="Decorative looped line ornament"></div>
    <p class="net-weight">295g/ 250ml</p>
  </section>

  <section class="label label--back" aria-label="Back label">
    <svg class="label__shape" viewBox="0 0 560 585" aria-hidden="true">
      <use href="#label-outline" class="label__fill"/>
      <use href="#label-outline" class="label__rule" transform="translate(280 292.5) scale(0.975) translate(-280 -292.5)"/>
    </svg>
    <div class="brand-name">Velombri</div>
    <p class="slogan">Apportez le vrai goût à votre maison</p>

    <p class="description">"Lorem ipsum dolor sit amet, consectetur adipiscing elit, sed do eiusmod tempor incididunt ut labore et dolore magna aliqua. Ut enim ad minim veniam, quis nostrud exercitation ullamco laboris nisi ut aliquip ex ea commodo consequat. Duis aute irure dolor in reprehenderit in voluptate velit esse cillum dolore eu fugiat nulla pariatur. Excepteur sint occaecat cupidatat non proident, sunt in culpa qui officia deserunt mollit anim id est laborum."</p>

    <div class="nutrition">
      <div class="nutrition__title">Nutrition Facts</div>
      <div>8 servings per container</div>
      <div class="nutrition__serving" style="display:flex;justify-content:space-between"><span>Serving size</span><span>2/3 cup (55g)</span></div>
      <div class="nutrition__bar"></div>
      <div style="font-weight:700;font-size:5.8px">Amount per serving</div>
      <div class="nutrition__calories"><span class="nutrition__calories-label">Calories</span><span class="nutrition__calories-value">230</span></div>
      <div class="nutrition__bar nutrition__bar--mid"></div>
      <div class="nutrition__dv" style="border-top:none">% Daily Value*</div>
      <div class="nutrition__row"><span><b>Total Fat</b> 8g</span><b>10%</b></div>
      <div class="nutrition__row nutrition__row--indent"><span>Saturated Fat 1g</span><b>5%</b></div>
      <div class="nutrition__row nutrition__row--indent"><span><i>Trans</i> Fat 0g</span><span></span></div>
      <div class="nutrition__row"><span><b>Cholesterol</b> 0mg</span><b>0%</b></div>
      <div class="nutrition__row"><span><b>Sodium</b> 160mg</span><b>7%</b></div>
      <div class="nutrition__row"><span><b>Total Carbohydrate</b> 37g</span><b>13%</b></div>
      <div class="nutrition__row nutrition__row--indent"><span>Dietary Fiber 4g</span><b>14%</b></div>
      <div class="nutrition__row nutrition__row--indent"><span>Total Sugars 12g</span><span></span></div>
      <div class="nutrition__row nutrition__row--indent2"><span>Includes 10g Added Sugars</span><b>20%</b></div>
      <div class="nutrition__row"><span><b>Protein</b> 3g</span><span></span></div>
      <div class="nutrition__bar"></div>
      <div class="nutrition__row nutrition__row--plain"><span>Vitamin D 2mcg</span><span>10%</span></div>
      <div class="nutrition__row"><span>Calcium 260mg</span><span>20%</span></div>
      <div class="nutrition__row"><span>Iron 8mg</span><span>45%</span></div>
      <div class="nutrition__row"><span>Potassium 235mg</span><span>6%</span></div>
      <div class="nutrition__bar nutrition__bar--mid"></div>
      <p class="nutrition__footnote">* The % Daily Value (DV) tells you how much a nutrient in a serving of food contributes to a daily diet. 2,000 calories a day is used for general nutrition advice.</p>
    </div>

    <div class="ingredients">
      <p>Ingredients:</p>
      <p>- fr: eau, graines de MOUTARDE, vinaigre d'alcool, sel, acidifiant : acide citrique, conservateur : E224 (SULFITES).</p>
      <p>En: water, MUSTARD seeds, alcohol vinegar, salt, acidifier: citric acid, preservative: E224 (SULFITES).</p>
    </div>
    <p class="packer">Conditioned by Sarl Velombri/conditionné par Sarl Velombri</p>
  </section>

</main>
</body>
</html>
```